Brightmoor Signal needs a Business Card

Designers!
More often than not, people want a cheap business card and often argue "I only want 100, not 500" - Years ago I worked in print and always wanted a client to ask for something that challenged me and would be great for my portfolio.

Years have past, and I dont have the time to do it myself so I'd love to see what everyone can offer.

Reason: Hey Guys, The designs are looking good but i've extended it a few more days as I wont be near a laptop and i'm trying to provide everyone feedback - Sorry!

Target Market(s)

Key decision makers, Potential Clients, Networking events and opportunities.

Industry/Entity Type

Business

Requirements
Must have
• Typography is very important. The type of paper is important.
The print, the shape. The creativity.
I'm very inspired by the below link
http://www.palevantro.com/blog/business-card-design/

Nice to have
• Stencelled cutouts. Embossing, nice typography.
I'd like the business card to be a conversation piece itself.

Attached is an image of business cards i've had in the past.
Additionally, some logos i've recently had designed by Quillmarsh.

```html
<!DOCTYPE html>
<html lang="en">
<head>
<meta charset="utf-8">
<title>Brightmoor Signal — Business Card</title>
<link rel="stylesheet" href="https://fonts.googleapis.com/css2?family=Ubuntu:wght@400&family=Advent+Pro:wght@300;400&family=Questrial&display=swap">
<style>
  :root{
    --backdrop:#0f4f7a;
    --frame-green:#9fc04c;
    --card-paper:#ebe9e8;
    --ink-navy:#273459;
    --rule-green:#a9c85a;
  }
  *{margin:0;padding:0;box-sizing:border-box}
  html,body{width:1200px;height:900px;overflow:hidden}
  body{background:var(--backdrop);position:relative;font-family:"Ubuntu",sans-serif;color:var(--ink-navy)}

  .card{position:absolute;background:var(--frame-green)}
  .card-face{position:absolute;background:var(--card-paper)}

  /* Front */
  .card--front{left:58px;top:123px;width:614px;height:401px}
  .card--front .card-face{left:21px;top:18px;width:572px;height:364px}
  .wordmark{position:absolute;left:142px;top:154px;width:290px;display:flex;align-items:center;gap:12px}
  .wordmark-square{width:20px;height:20px;background:var(--frame-green);flex:none}
  .wordmark-name{font-size:25px;line-height:30px;letter-spacing:0.5px;text-transform:uppercase;white-space:nowrap}
  .wordmark-rule{position:absolute;left:142px;top:202px;width:288px;height:1px;background:var(--ink-navy);opacity:.55}
  .wordmark-url{position:absolute;left:142px;top:207px;width:288px;line-height:16px;text-align:center;font-family:"Questrial",sans-serif;font-size:12px;letter-spacing:4.6px;color:var(--frame-green)}

  /* Back */
  .card--back{left:702px;top:123px;width:441px;height:674px}
  .card--back .card-face{left:20px;top:22px;width:401px;height:632px}

  .block{position:absolute;left:71px;width:264px}
  .rule{position:absolute;left:71px;width:264px;height:1px;background:var(--rule-green)}
  .rule-double{position:absolute;left:71px;width:264px;height:8px;border-top:1px solid var(--rule-green);border-bottom:1px solid var(--rule-green)}

  .person-name{top:103px;height:26px;line-height:26px;text-align:center;font-size:21px;font-weight:400;letter-spacing:1.2px;white-space:nowrap}
  .person-title{top:138px;height:28px;line-height:28px;text-align:center;font-size:22px;letter-spacing:.6px;white-space:nowrap}

  .row{display:flex;align-items:center;white-space:nowrap}
  .row--phone{top:298px;height:50px;gap:6px}
  .row--phone svg{flex:none}
  .phone-number{display:block;flex:none;font-family:"Advent Pro",sans-serif;font-weight:300;font-size:62px;line-height:50px;letter-spacing:1px;transform:scaleX(.72);transform-origin:left center;width:212px}
  .row--web{top:363px;height:20px;font-size:15px;line-height:20px;gap:18px;padding-left:2px}
  .row--web svg{flex:none}
  .row--social{top:405px;height:30px;font-family:"Questrial",sans-serif;font-size:18px;line-height:30px;letter-spacing:2.6px;gap:12px}
  .social-dot{width:28px;height:28px;border-radius:50%;background:var(--ink-navy);flex:none;margin-left:2px}
  .row--email{top:453px;height:20px;justify-content:center;font-family:"Advent Pro",sans-serif;font-weight:400;font-size:17px;line-height:20px;letter-spacing:1px;text-transform:uppercase}
  .address{top:494px;font-family:"Questrial",sans-serif;font-size:15.5px;letter-spacing:1.2px;line-height:20px;text-transform:uppercase;white-space:nowrap}
  .address-line{display:flex;align-items:center;gap:10px;height:20px}
  .address-line svg{flex:none}
</style>
</head>
<body>

  <section class="card card--front" aria-label="Card front">
    <div class="card-face">
      <div class="wordmark">
        <span class="wordmark-square" aria-hidden="true"></span>
        <span class="wordmark-name">Brightmoor Signal</span>
      </div>
      <div class="wordmark-rule"></div>
      <div class="wordmark-url">brightmoorsignal.com.au</div>
    </div>
  </section>

  <section class="card card--back" aria-label="Card back">
    <div class="card-face">
      <h1 class="block person-name">DORIAN VELLACOTT</h1>
      <div class="rule" style="top:133px"></div>
      <p class="block person-title">Consultant &amp; Educator</p>

      <div class="rule-double" style="top:285px"></div>
      <div class="block row row--phone">
        <svg width="46" height="42" viewBox="0 0 46 42" aria-hidden="true">
          <path d="M2 14 C2 4 44 4 44 14 L44 18 L33 18 L33 13 L13 13 L13 18 L2 18 Z" fill="#273459"/>
          <path d="M9 20 L37 20 L43 40 L3 40 Z" fill="#273459"/>
          <circle cx="23" cy="29" r="7" fill="#ebe9e8"/>
          <circle cx="23" cy="29" r="3.5" fill="#273459"/>
        </svg>
        <span class="phone-number">555.013.2948</span>
      </div>
      <div class="rule" style="top:353px"></div>

      <div class="block row row--web">
        <svg width="15" height="15" viewBox="0 0 16 16" aria-hidden="true">
          <circle cx="8" cy="8" r="7.5" fill="#273459"/>
          <path d="M4 4 Q7 5 6 8 Q4 10 5 13 M10 3 Q11 6 13 7 M9 10 Q11 11 11 14" stroke="#ebe9e8" stroke-width="1.4" fill="none"/>
        </svg>
        <span>www.theloanledgerguy.org</span>
      </div>

      <div class="block row row--social">
        <span class="social-dot" aria-hidden="true"></span>
        <span>@TheLedgerGuy</span>
      </div>

      <div class="rule-double" style="top:444px"></div>
      <div class="block row row--email" style="top:454px">dorian@theloanledgerguy.org</div>
      <div class="rule" style="top:481px"></div>

      <div class="block address">
        <div class="address-line">
          <svg width="11" height="16" viewBox="0 0 11 16" aria-hidden="true">
            <path d="M5.5 0 C2.5 0 0 2.4 0 5.4 C0 9.4 5.5 16 5.5 16 C5.5 16 11 9.4 11 5.4 C11 2.4 8.5 0 5.5 0 Z" fill="#273459"/>
            <circle cx="5.5" cy="5.4" r="2.2" fill="#ebe9e8"/>
          </svg>
          <span>1180 W. Harlow Ave</span>
        </div>
        <div class="address-line">Suite C, Fenbrook, CA 90417</div>
      </div>
      <div class="rule-double" style="top:542px"></div>
    </div>
  </section>

</body>
</html>
```